Flyer Design Project

We are a mortgage company Bramwell Lending Corp. that will be looking to mail out these flyers to promote Reverse Mortgages. Some clip art of Seniors (Happy Smile having a good time) Our phone number on the flyer in a few places 877-260-5718
Text: No Celebrity Endorsers or talking heads here
Solutions for seniors... Stop worrying Start Living
Say Goodby to monthly payments with a reverse mortgage
The Loan That Pays You
Secure Your Retirement With A Reverse Mortgage
NLB Goverment Insured
Retain Complete ownership of your Home
Save and Effective Financial Tool
Pay Off Credit cards Elimanate Mortgage payments improve your home or lifestyle
No Credit score or income requirements
Faceing a foreclosure a reverse mortgage can help
Is a reverse mortgage right for you? Get the facts from a qualified reverse mortgage originator
The text above does not have to be in that order
I am having trouble with my Logo so i am getting a new file and will be able to upload it to the flyer shortly just leave room for it
Seniors over the age of 62
Financial

```html
<!DOCTYPE html>
<html lang="en">
<head>
<meta charset="utf-8">
<title>Reverse Mortgage Flyer – Bramwell Lending Corp.</title>
<link href="https://fonts.googleapis.com/css2?family=Tinos:wght@400;700&display=swap" rel="stylesheet">
<style>
  :root {
    --page: #ffffff;
    --navy: #23405f;
    --magenta: #e0139a;
    --magenta-light: #f25cc0;
    --magenta-dark: #a0066c;
    --text-light: #ffffff;
    --text-soft: #dbe4ee;
  }
  * { margin: 0; padding: 0; box-sizing: border-box; }
  html, body {
    width: 972px; height: 1200px; overflow: hidden;
    background: var(--page);
  }
  .canvas { position: relative; width: 972px; height: 1200px; background: var(--page); }
  .flyer {
    position: absolute; left: 65px; top: 61px;
    width: 838px; height: 1083px; overflow: hidden;
    background: var(--navy);
  }
  .flyer-art { position: absolute; inset: 0; width: 838px; height: 1083px; display: block; }
  .headline {
    position: absolute; left: 77px; top: 632px;
    font-family: "Tinos", "Times New Roman", serif;
    font-weight: 400; font-size: 50px; line-height: 57px;
    color: var(--text-light); letter-spacing: -0.5px;
    white-space: nowrap;
  }
  .headline-highlight {
    background: var(--magenta);
    padding: 0 8px 0 6px;
  }
  .benefits {
    position: absolute; left: 77px; top: 772px; width: 720px;
    list-style: none;
    font-family: "Tinos", "Times New Roman", serif;
    font-size: 15px; line-height: 21.4px;
    color: var(--text-soft);
    white-space: nowrap;
  }
  .benefit-sep {
    display: inline-block; width: 0; height: 0;
    border-top: 5px solid transparent; border-bottom: 5px solid transparent;
    border-left: 7px solid var(--text-light);
    margin: 0 6px 0 5px; vertical-align: 0;
  }
  .benefit-phone { color: var(--text-light); font-weight: 700; }
  .contact-line {
    position: absolute; left: 77px; top: 982px;
    font-family: "Tinos", "Times New Roman", serif;
    font-size: 25px; line-height: 32px;
    color: var(--text-light);
    white-space: nowrap;
  }
  .contact-phone {
    background: var(--magenta);
    padding: 0 5px;
  }
  .logo-space {
    position: absolute; left: 560px; top: 960px;
    width: 230px; height: 95px;
  }
</style>
</head>
<body>
<div class="canvas">
  <section class="flyer">
    <svg class="flyer-art" viewBox="0 0 838 1083" xmlns="http://www.w3.org/2000/svg">
      <defs>
        <linearGradient id="photoTone" x1="0" y1="0" x2="1" y2="0.6">
          <stop offset="0" stop-color="#d9e6ef"/>
          <stop offset="0.3" stop-color="#4f8fd0"/>
          <stop offset="0.55" stop-color="#eef2f4"/>
          <stop offset="0.8" stop-color="#d8c7bc"/>
          <stop offset="1" stop-color="#c9b2a6"/>
        </linearGradient>
        <linearGradient id="panelTone" x1="0" y1="0" x2="0" y2="1">
          <stop offset="0" stop-color="#1a3553"/>
          <stop offset="0.5" stop-color="#24425f"/>
          <stop offset="1" stop-color="#1f3b58"/>
        </linearGradient>
        <linearGradient id="waveTone" x1="0" y1="0" x2="1" y2="0">
          <stop offset="0" stop-color="#c40a86"/>
          <stop offset="0.45" stop-color="#f04cbc"/>
          <stop offset="1" stop-color="#b8087c"/>
        </linearGradient>
      </defs>

      <rect class="photo-area" x="0" y="0" width="838" height="600" fill="url(#photoTone)" role="img" aria-label="Photo of a smiling caregiver feeding a happy senior woman with a spoon"/>

      <path class="wave-magenta" d="M0 334 C 180 360, 320 470, 520 470 C 650 470, 760 430, 838 400 L 838 600 L 0 600 Z" fill="url(#waveTone)"/>
      <path class="wave-sheen" d="M0 372 C 200 400, 330 505, 540 500 C 670 497, 770 460, 838 440 L 838 470 C 770 490, 670 525, 540 528 C 330 532, 200 430, 0 410 Z" fill="var(--magenta-light)" opacity="0.45"/>
      <path class="wave-shadow" d="M0 430 C 210 450, 330 545, 560 548 C 690 550, 780 520, 838 505 L 838 600 L 0 600 Z" fill="var(--magenta-dark)" opacity="0.7"/>

      <path class="info-panel" d="M0 466 C 210 478, 340 585, 570 588 C 700 590, 790 560, 838 548 L 838 1083 L 0 1083 Z" fill="url(#panelTone)"/>
    </svg>

    <h1 class="headline">Solutions for <span class="headline-highlight">Seniors</span><br>Stop worrying, start living</h1>

    <ul class="benefits">
      <li>No Celebrity Endorsers or talking heads here</li>
      <li>Seniors over the age of 62<span class="benefit-sep"></span>NLB Goverment Insured</li>
      <li>Say Goodby to monthly payments with a reverse mortgage</li>
      <li>Secure Your Retirement With A Reverse Mortgage<span class="benefit-sep"></span>The Loan That Pays You</li>
      <li>Retain Complete ownership of your Home<span class="benefit-sep"></span>Save and Effective Financial Tool</li>
      <li>Pay Off Credit cards Elimanate Mortgage payments improve your home or lifestyle</li>
      <li>No Credit score or income requirements<span class="benefit-sep"></span>Faceing a foreclosure a reverse mortgage can help</li>
      <li>Is a reverse mortgage right for you? Get the facts from a qualified reverse mortgage originator</li>
      <li>Call Bramwell Lending Corp. today<span class="benefit-sep"></span><span class="benefit-phone">877-260-5718</span></li>
    </ul>

    <p class="contact-line">Call today <span class="contact-phone">877-260-5718</span></p>

    <div class="logo-space" role="img" aria-label="Reserved space for the Bramwell Lending Corp. logo"></div>
  </section>
</div>
</body>
</html>
```